Medical Staffing agency

I need a logo design that can stand along and become a brand. I'm not too particular of the design. Want something catchy and hopefully related to the Health field. Not important though. An example of what I'm looking for is the Stride Forge Logo, or the Vantora Logo. Something that can become a brand without having to say the brand name. A bit about my company, I hire medical staff, and contract with other companies to provide anywhere from short term to long term employees. But that is expanding to more than just that.

Industry/Entity Type

Medical

Contact Information for Business Card

Westmere Rehab Services
Dalen Whitcombe, CEO
742 Brookhollow Ave
Suite 48
Fairvale, WR 95718

```html
<!DOCTYPE html>
<html lang="en">
<head>
<meta charset="utf-8">
<title>Westmere Rehab Services – Business Card</title>
<link rel="stylesheet" href="https://fonts.googleapis.com/css2?family=Lato:wght@400;700;900&display=swap">
<style>
  :root {
    --card-bg: #c7e8f8;
    --brand-blue: #1aa3dc;
    --mark-blue: #1aa6e4;
    --ink: #111111;
  }
  * { margin: 0; padding: 0; box-sizing: border-box; }
  html, body {
    width: 1200px;
    height: 702px;
    overflow: hidden;
    background: var(--card-bg);
  }
  .card {
    position: relative;
    width: 1200px;
    height: 702px;
    background: var(--card-bg);
    font-family: "Lato", "Helvetica Neue", Arial, sans-serif;
    color: var(--ink);
  }
  .brand {
    position: absolute;
    left: 52px;
    top: 52px;
    display: flex;
    align-items: center;
  }
  .brand-mark {
    width: 170px;
    height: 160px;
    flex: none;
  }
  .brand-name {
    margin-left: 26px;
    font-size: 31px;
    font-weight: 400;
    color: var(--brand-blue);
    letter-spacing: 0.2px;
  }
  .contact {
    position: absolute;
    right: 64px;
    top: 431px;
    width: 940px;
    text-align: right;
  }
  .contact-company {
    font-size: 40px;
    font-weight: 900;
    line-height: 1.2;
    margin-bottom: 20px;
  }
  .contact-details {
    font-size: 37px;
    font-weight: 400;
    line-height: 85px;
  }
</style>
</head>
<body>
  <main class="card">
    <header class="brand">
      <svg class="brand-mark" viewBox="0 0 170 160" aria-hidden="true">
        <circle cx="86" cy="77" r="73" fill="var(--mark-blue)"/>
      </svg>
      <span class="brand-name">Westmere Rehab Services LLC</span>
    </header>

    <section class="contact">
      <h1 class="contact-company">Westmere Rehab Services</h1>
      <p class="contact-details">Dalen Whitcombe, CEO 742 Brookhollow Ave Suite 48 Fairvale, WR 95718</p>
    </section>
  </main>
</body>
</html>
```